R&T Promotions / P.L.W. Sales Business Cards

I have 2 companies that are somewhat connected, yet sell to 2 different markets.

R&T Promotions www.rotapfx.example

We are a manufacturers representative company. We handle sales and marketing of Home Theater, Home Automation, Audio & Video products for the state of Florida. We work with Designers, Architects, Technology Consultants and Electronic Integrators to design, sell and install cutting edge technology in new and existing homes, condos and commercial spaces.

P.L.W. Sales www.plwqz.example

We are a manufacturers representative company. We handle sales and marketing of automotive Audio, Electronics, Security, Navigation and Entertainment products for the state of Florida. We work with 12-volt retailers, installers and automobile customizers to design, sell, merchandise, fabricate and install cutting edge technology in cars, boats, motor coaches, etc.

We have logo's that might still be relevant, but might need a little touching up. We need a new business card design and layout for each of the 2 companies. I would like them to have a family look, but still better speak to the customer base associated with the channel.

Target Market(s)

R&T Promotions -

Design, Engineering, Construction, Technology, elegant, tasteful.

P.L.W. Sales -

More cutting edge, industrial, youth, aggressive, fun, bold.

Industry/Entity Type

Business

Requirements
Must have
• New business card layout for both companies.
Nice to have
• A family look, or relationship to the other company. Even if it's just a logo referencing the other company.

```html
<!DOCTYPE html>
<html lang="en">
<head>
<meta charset="utf-8">
<title>R&amp;T Promotions / P.L.W. Sales Business Cards</title>
<link href="https://fonts.googleapis.com/css2?family=Cinzel:wght@400&family=Arimo:wght@400;700&display=swap" rel="stylesheet">
<style>
  :root {
    --backdrop: #3b302a;
    --label: #ffffff;
    --card-white: #ffffff;
    --card-grey: #71777a;
    --card-light: #e6e7e8;
    --band: #e3e4e5;
    --ink: #231f20;
    --ink-soft: #6b6d6f;
    --rule: #9a9c9e;
    --pill-dark: #141414;
    --pill-grey: #7b7f82;
    --logo-light: #ececec;
  }
  * { margin: 0; padding: 0; box-sizing: border-box; }
  html, body { width: 1200px; height: 747px; overflow: hidden; }
  body {
    position: relative;
    background: var(--backdrop);
    font-family: "Arimo", Arial, sans-serif;
  }
  .card { position: absolute; width: 476px; height: 271px; overflow: hidden; }
  .card--front { left: 104px; top: 95px; background: var(--card-white); }
  .card--back-1 { left: 621px; top: 96px; background: var(--card-grey); }
  .card--back-2 { left: 102px; top: 405px; background: var(--card-white); }
  .card--back-3 { left: 630px; top: 405px; background: var(--card-light); }

  .view-label {
    position: absolute;
    color: var(--label);
    font-size: 31px;
    font-family: "Arimo", Arial, sans-serif;
  }
  .view-label--1 { left: 976px; top: 40px; }
  .view-label--2 { left: 104px; top: 694px; }
  .view-label--3 { left: 975px; top: 690px; }

  .brand-rt {
    position: absolute;
    font-family: "Cinzel", "Times New Roman", serif;
    font-weight: 400;
    color: var(--ink);
    text-align: center;
    line-height: 1.05;
    font-size: 25px;
    letter-spacing: 1px;
  }
  .brand-rt span { display: block; }
  .brand-rt .brand-rt__mark { font-size: 25px; letter-spacing: 4px; }

  .brand-plw {
    position: absolute;
    font-family: "Cinzel", "Times New Roman", serif;
    font-weight: 400;
    color: var(--ink);
    text-align: center;
    line-height: 1.1;
  }
  .brand-plw span { display: block; }

  .divider { position: absolute; width: 2px; background: var(--rule); }

  /* front */
  .card--front .brand-rt { left: 34px; top: 62px; width: 190px; }
  .card--front .divider { left: 243px; top: 38px; height: 117px; }
  .contact-list { position: absolute; left: 279px; top: 38px; list-style: none; }
  .contact-list li {
    display: flex; align-items: center; gap: 6px;
    height: 17px; font-size: 11.5px; color: var(--ink-soft);
  }
  .contact-list svg { width: 10px; height: 10px; fill: var(--ink-soft); flex: none; }
  .address {
    position: absolute; left: 278px; top: 133px;
    font-size: 11.5px; line-height: 14px; color: var(--ink-soft); font-style: normal;
  }
  .front-band {
    position: absolute; left: 0; top: 205px; width: 100%; height: 66px; background: var(--band);
  }
  .front-band .brand-plw { left: 10px; top: 14px; width: 92px; font-size: 15px; }
  .name-pill {
    position: absolute; left: 141px; top: 222px; height: 28px; width: 210px;
    background: var(--pill-dark); border-radius: 14px;
    color: #fff; font-family: "Cinzel", "Times New Roman", serif; font-size: 16px;
    letter-spacing: 1px; display: flex; align-items: center; justify-content: center;
  }
  .title-pill {
    position: absolute; left: 344px; top: 222px; height: 28px; width: 140px;
    background: var(--pill-grey); border-radius: 14px 0 0 14px;
    color: #fff; font-size: 13.5px; display: flex; align-items: center; padding-left: 18px;
  }

  /* back 1 */
  .card--back-1 .brand-rt { left: 30px; top: 148px; width: 180px; color: var(--logo-light); font-size: 27px; }
  .card--back-1 .brand-plw { left: 282px; top: 166px; width: 146px; font-size: 22px; color: var(--ink); }
  .web {
    position: absolute; font-size: 11px; letter-spacing: 2px;
  }
  .card--back-1 .web { left: 264px; top: 239px; color: #fff; }

  /* back 2 */
  .card--back-2 .brand-rt { left: 50px; top: 96px; width: 190px; font-size: 27px; }
  .card--back-2 .divider { left: 255px; top: 63px; height: 145px; background: #c9cacb; }
  .card--back-2 .brand-plw { left: 280px; top: 106px; width: 130px; font-size: 22px; }

  /* back 3 */
  .card--back-3 .brand-rt { left: 143px; top: 88px; width: 190px; font-size: 27px; }
  .card--back-3 .web {
    left: 0; width: 100%; top: 241px; text-align: center; color: var(--ink-soft);
    letter-spacing: 4.5px; font-size: 11.5px;
  }
</style>
</head>
<body>
  <div class="view-label view-label--1">Back 1</div>
  <div class="view-label view-label--2">Back 2</div>
  <div class="view-label view-label--3">Back 3</div>

  <section class="card card--front">
    <div class="brand-rt"><span class="brand-rt__mark">R&amp;T</span><span>PROMOTIONS</span></div>
    <div class="divider"></div>
    <ul class="contact-list">
      <li><svg viewBox="0 0 10 10"><rect x="3" y="0" width="4" height="10" rx="1"/></svg>555-014-1281</li>
      <li><svg viewBox="0 0 10 10"><circle cx="5" cy="5" r="4.5" fill="none" stroke="#6b6d6f"/><path d="M3 3h2l-1 2 2 2h1v1H6L3 5z"/></svg>800-555-017</li>
      <li><svg viewBox="0 0 10 10"><rect x="2" y="0" width="6" height="3"/><rect x="0" y="3" width="10" height="5" rx="1"/></svg>555-019-7932</li>
      <li><svg viewBox="0 0 10 10"><rect x="0" y="2" width="10" height="6"/></svg>dana@rt-plw.example</li>
      <li><svg viewBox="0 0 10 10" fill="none" stroke="#6b6d6f"><circle cx="5" cy="5" r="4.5"/><ellipse cx="5" cy="5" rx="2" ry="4.5"/><path d="M0.5 5h9"/></svg>http://www.rt-plw.example</li>
    </ul>
    <address class="address">4120 Harbor Line Ave,<br>Coral Vale, FL 30100</address>
    <div class="front-band">
      <div class="brand-plw"><span>P.L.W.</span><span>SALES</span></div>
    </div>
    <div class="title-pill">Rep Principle</div>
    <div class="name-pill">DANA WHITFIELD</div>
  </section>

  <section class="card card--back-1">
    <div class="brand-rt"><span class="brand-rt__mark">R&amp;T</span><span>PROMOTIONS</span></div>
    <div class="brand-plw"><span>P.L.W.</span><span>SALES</span></div>
    <div class="web">http://www.rt-plw.example</div>
  </section>

  <section class="card card--back-2">
    <div class="brand-rt"><span class="brand-rt__mark">R&amp;T</span><span>PROMOTIONS</span></div>
    <div class="divider"></div>
    <div class="brand-plw"><span>P.L.W.</span><span>SALES</span></div>
  </section>

  <section class="card card--back-3">
    <div class="brand-rt"><span class="brand-rt__mark">R&amp;T</span><span>PROMOTIONS</span></div>
    <div class="web">http://www.rt-plw.example</div>
  </section>
</body>
</html>
```